Customer Journey Graphic

I want to graphic to describe a marketing framework I am teaching a course on

It a framework for growing a business
The idea is we
get customers to "take a Journey" through 7 steps
to deliver value to them

There are 4 major concepts that impact this journey - Game Plan, Business Model, "Inside out thinking' and Unique Competitive advantage
These concepts can make the journey faster, get more people to take it or make it more valuable

The stages are

- Target
- attract
- nurture
- convert
- maximise
- loyalty
- reactivation

I want to uses this framework as an overall;; 'explainer' fro my idea ,so it must looks very professional, and work well in presentations

I have included a rought 'sketch; of my thinking as an attachment

Business Owners

Business

Serif

• clear, get acroess the idea of a Journye over times, teh idea you can improve your results throught applying concpets of ' business model', "inside out thinking: , unique competitive advantage and game plane

```html
<!DOCTYPE html>
<html lang="en">
<head>
<meta charset="utf-8">
<title>Growing a Business – Customer Journey</title>
<link rel="stylesheet" href="https://fonts.googleapis.com/css2?family=Roboto+Condensed:wght@400;500;700&display=swap">
<style>
  :root {
    --ink: #111111;
    --blue: #3b55a5;
    --gold: #d89b2c;
    --bg-light: #f6f6f6;
    --bg-dark: #e2e2e2;
    --tile: #ffffff;
    --step-1: #6fa2b8;
    --step-2: #2fb98b;
    --step-3: #1689b0;
    --step-4: #1db48b;
    --step-5: #1b5e79;
    --step-6: #128a6a;
    --step-7: #154b62;
  }
  html, body {
    margin: 0;
    padding: 0;
    width: 1200px;
    height: 1200px;
    overflow: hidden;
  }
  .canvas {
    position: relative;
    width: 1200px;
    height: 1200px;
    background: radial-gradient(circle at 60% 40%, var(--bg-light) 0%, #eeeeee 55%, var(--bg-dark) 100%);
    font-family: "Roboto Condensed", "Arial Narrow", sans-serif;
  }
  .edge-strip {
    position: absolute;
    left: 0;
    top: 0;
    width: 53px;
    height: 1200px;
    background: linear-gradient(90deg, #fafafa, #f0f0f0);
    box-shadow: 3px 0 6px rgba(0,0,0,0.18);
  }
  .artwork {
    position: absolute;
    inset: 0;
    width: 1200px;
    height: 1200px;
  }
  .title { font-weight: 500; font-size: 66px; fill: var(--ink); letter-spacing: 1px; }
  .sub { font-weight: 400; font-size: 25px; fill: var(--blue); }
  .steps-count { font-weight: 700; font-size: 56px; fill: var(--blue); }
  .journey { font-weight: 700; font-size: 58px; fill: var(--gold); letter-spacing: 1px; }
  .concepts-head { font-weight: 700; font-size: 27px; fill: var(--ink); }
  .concepts { font-weight: 400; font-size: 21px; fill: var(--ink); }
  .step-label { font-weight: 400; font-size: 34px; fill: #ffffff; }
  .step-rule { stroke: rgba(255,255,255,0.35); stroke-width: 1; }
</style>
</head>
<body>
<div class="canvas">
  <div class="edge-strip"></div>

  <svg class="artwork" viewBox="0 0 1080 1080" xmlns="http://www.w3.org/2000/svg">
    <defs>
      <filter id="soft-shadow" x="-30%" y="-30%" width="160%" height="160%">
        <feDropShadow dx="4" dy="6" stdDeviation="6" flood-color="#000" flood-opacity="0.28"/>
      </filter>
      <linearGradient id="tile-face" x1="0" y1="0" x2="1" y2="1">
        <stop offset="0" stop-color="#ffffff"/>
        <stop offset="1" stop-color="#e9e9e9"/>
      </linearGradient>
    </defs>

    <!-- Header -->
    <g class="header" text-anchor="middle">
      <text class="title" x="572" y="96">GROWING A BUSINESS</text>
      <text class="sub" x="570" y="135">GET CUSTOMERS TO  THROUGH</text>
      <text class="steps-count" x="572" y="206">7 STEPS</text>
      <text class="sub" x="570" y="242">TO DELIVER VALUE TO THEM</text>
      <text class="journey" x="570" y="305">TAKE A JOURNEY</text>
      <text class="concepts-head" x="570" y="352">THERE ARE 4 MAJOR CONCEPTS THAT IMPACT THIS JOURNEY</text>
      <text class="concepts" x="572" y="383">GAME PLAN  |  BUSINESS MODEL  |  INSIDE OUT THINING  |  UNIQUE COMPETITIVE ADVANTAGE</text>
    </g>

    <!-- Journey bands -->
    <g class="journey-bands" filter="url(#soft-shadow)">
      <rect x="48" y="447" width="372" height="81" fill="var(--step-1)"/>
      <rect x="48" y="527" width="500" height="81" fill="var(--step-2)"/>
      <rect x="48" y="607" width="640" height="81" fill="var(--step-3)"/>
      <rect x="48" y="687" width="530" height="81" fill="var(--step-4)"/>
      <rect x="48" y="767" width="415" height="81" fill="var(--step-5)"/>
      <rect x="48" y="847" width="610" height="81" fill="var(--step-6)"/>
      <rect x="48" y="927" width="400" height="81" fill="var(--step-7)"/>
    </g>

    <g class="band-rules">
      <line class="step-rule" x1="128" y1="458" x2="345" y2="458"/><line class="step-rule" x1="128" y1="516" x2="345" y2="516"/>
      <line class="step-rule" x1="128" y1="538" x2="465" y2="538"/><line class="step-rule" x1="128" y1="596" x2="465" y2="596"/>
      <line class="step-rule" x1="128" y1="618" x2="465" y2="618"/><line class="step-rule" x1="128" y1="676" x2="465" y2="676"/>
      <line class="step-rule" x1="128" y1="698" x2="465" y2="698"/><line class="step-rule" x1="128" y1="756" x2="465" y2="756"/>
      <line class="step-rule" x1="128" y1="778" x2="385" y2="778"/><line class="step-rule" x1="128" y1="836" x2="385" y2="836"/>
      <line class="step-rule" x1="128" y1="858" x2="380" y2="858"/><line class="step-rule" x1="128" y1="916" x2="380" y2="916"/>
      <line class="step-rule" x1="128" y1="938" x2="375" y2="938"/><line class="step-rule" x1="128" y1="996" x2="375" y2="996"/>
    </g>

    <g class="step-labels">
      <text class="step-label" x="66" y="501">01  TARGET</text>
      <text class="step-label" x="66" y="581">02  ATTRACT</text>
      <text class="step-label" x="66" y="661">03  NURTURE</text>
      <text class="step-label" x="66" y="741">04  CONVERT</text>
      <text class="step-label" x="66" y="821">05  MAXIMISE</text>
      <text class="step-label" x="66" y="901">06  LOYALTY</text>
      <text class="step-label" x="66" y="981">07  REACTIVATION</text>
    </g>

    <!-- Step tiles -->
    <g class="step-tiles" filter="url(#soft-shadow)">
      <rect x="-48" y="-48" width="96" height="96" rx="6" fill="url(#tile-face)" transform="translate(422 487) rotate(45)"/>
      <rect x="-48" y="-48" width="96" height="96" rx="6" fill="url(#tile-face)" transform="translate(548 567) rotate(45)"/>
      <rect x="-48" y="-48" width="96" height="96" rx="6" fill="url(#tile-face)" transform="translate(690 647) rotate(45)"/>
      <rect x="-48" y="-48" width="96" height="96" rx="6" fill="url(#tile-face)" transform="translate(580 727) rotate(45)"/>
      <rect x="-48" y="-48" width="96" height="96" rx="6" fill="url(#tile-face)" transform="translate(462 807) rotate(45)"/>
      <rect x="-48" y="-48" width="96" height="96" rx="6" fill="url(#tile-face)" transform="translate(656 887) rotate(45)"/>
      <rect x="-48" y="-48" width="96" height="96" rx="6" fill="url(#tile-face)" transform="translate(452 967) rotate(45)"/>
    </g>

    <!-- Illustration areas -->
    <g class="step-illustrations">
      <circle cx="420" cy="487" r="30" fill="#b8272c" role="img" aria-label="Target board with a dart"/>
      <rect x="522" y="440" width="50" height="170" rx="10" fill="#2a2a2a" role="img" aria-label="Business person holding up a gold coin"/>
      <rect x="650" y="575" width="80" height="105" rx="10" fill="#3f4b55" role="img" aria-label="Business person beside a location pin"/>
      <rect x="538" y="640" width="84" height="112" rx="10" fill="#2c2c2c" role="img" aria-label="Two business people shaking hands"/>
      <rect x="440" y="735" width="42" height="120" rx="10" fill="#2c2c2c" role="img" aria-label="Business person looking through a magnifying glass"/>
      <circle cx="656" cy="887" r="32" fill="#8e1f1f" role="img" aria-label="Red wax warranty seal with cord"/>
      <circle cx="452" cy="967" r="32" fill="#e3b22a" role="img" aria-label="Gold dollar coin"/>
    </g>
  </svg>
</div>
</body>
</html>
```